Corporate Financial Services

This is a new Company. The ORV represents my son's and my own Christian name initials (ORV) (Colin and Neil) but no real significance.
This is a boutique financial services company active in the full parameter of corporate and business transactions. From standard financial and tax services to specialised Research & Development, mergers and acquisitions, business valuations, and capital raising.
Over 30 years of experience with listed and private entities.
I am after something exciting, given the nature of the business, bright, clean and colourful, but not in comic form.
Updates
Hi there,
Firstly thankyou for accepting the challenge. I have no ideas and nothing to compare your submissions with other than other peoples cards.
A few points
I omitted the ABN number from the card description. This is an important reference for all businesses operating in Australia. Therefore the following should be shown in association with the company name ORV Corporate & Financial Services Pty Ltd It can either be within brackets or without but always shown underneath the company name in smaller font.
The eight core business services need to be shown on the reverse
My contact number should also be shown along side the address
My business title is Chartered Accountant in full. I am also not fussed as to whether my name appears in caps or Caps and lowercase ie Neil Barrow or NEIL BARROW but this will depend upon the design of the rest of the card.
Maybe a small logo for the company needs to be attached but not sure.
Kind regards
Neil Barrow
Industry/Entity Type
Financial
Contact Information for Business Card
ORV Corporate & Financial Services Pty Ltd
(ABN 71 384 902 157)
(Note ABN could be shown on the reverse side with just ORV Corporate & Financial Services Pty Ltd on the front....no ABN
17 Wattlebank Road Wattlebank SA 5164
Neil Barrow
Chartered Accountant
Phone (symbol preferred) +61 (0) 437 215086
Email (symbol) to be provided
www.orv-example.com.au
Skype neil7312
Requirements
Must have
- On the reverse:
Corporate Finance
Taxation
Research & Development Specialisation
Financial Accounting
Mergers & Acquisitions
Company Listings (IPO's)
Business Valuations
Capital Raising
Nice to have
- Interested in a strong black card (or grey white platinum and black colours) with either platinum or gold highlight modern name style no italics. I would also like at a later stage with the winner to use this same design for card for Asia with a red and or gold and platinum colour. But I want this batch first.
The smart block (square) for digital image transfer to mobile phones contained within a gold or platinum square border on reverse of the card
Should not have
Anything old or staid looking. No italics sans serif

```html
<!DOCTYPE html>
<html lang="en">
<head>
<meta charset="utf-8">
<title>ORV Corporate &amp; Financial Services – Stationery</title>
<link rel="stylesheet" href="https://fonts.googleapis.com/css2?family=Lato:wght@400;700;900&family=Arimo:wght@400&display=swap">
<style>
  :root {
    --backdrop: #cddde8;
    --paper: #ffffff;
    --ink: #3a3a3a;
    --ink-soft: #555555;
    --gold: #c9a45c;
    --gold-light: #e2c68a;
    --card: #1f1f1f;
    --card-text: #f2f2f2;
    --rule: #8a8a8a;
    --sign-blue: #2f6fa8;
  }
  * { box-sizing: border-box; margin: 0; padding: 0; }
  html, body { width: 1200px; height: 900px; overflow: hidden; }
  body { background: var(--backdrop); position: relative; font-family: "Lato", sans-serif; }

  .letterhead {
    position: absolute; left: 43px; top: 18px; width: 669px; height: 862px;
    background: var(--paper); box-shadow: 0 2px 6px rgba(0,0,0,.18);
  }
  .letterhead__tab {
    position: absolute; right: 0; top: 47px; width: 24px; height: 83px;
    background: var(--gold); border-radius: 8px 0 0 8px;
  }
  .letterhead__brand { position: absolute; left: 62px; top: 55px; }
  .brand-name {
    font-family: "Lato", sans-serif; font-weight: 900; color: var(--gold);
    letter-spacing: 6px; line-height: 1;
  }
  .letterhead .brand-name { font-size: 64px; }
  .brand-legal { font-family: "Lato", sans-serif; font-weight: 700; color: var(--gold); white-space: nowrap; }
  .letterhead .brand-legal { font-size: 9px; margin-top: 4px; }

  .letterhead__contact {
    position: absolute; right: 36px; top: 58px; list-style: none;
    font-family: "Lato", sans-serif; font-size: 13px; color: var(--ink); text-align: right;
  }
  .letterhead__contact li { height: 15px; line-height: 15px; display: flex; justify-content: flex-end; align-items: center; gap: 8px; }
  .icon { width: 12px; height: 12px; flex: none; }

  .letter {
    position: absolute; left: 65px; top: 239px; width: 530px;
    font-family: "Arimo", sans-serif; font-size: 10.4px; line-height: 13px; color: var(--ink-soft);
  }
  .letter p { margin-bottom: 13px; }
  .letter__date { margin-bottom: 24px !important; }
  .signature-area {
    width: 156px; height: 30px; margin: 0 0 8px 2px;
    background: linear-gradient(90deg, rgba(47,111,168,.55), rgba(47,111,168,.15));
    border-radius: 14px;
  }
  .letter__sender p { margin: 0; }
  .letterhead__footer {
    position: absolute; left: 0; right: 0; bottom: 14px; text-align: center;
    font-family: "Lato", sans-serif; font-size: 13px; color: var(--ink);
  }

  .card {
    position: absolute; left: 736px; width: 441px; height: 251px;
    background: var(--card); color: var(--card-text);
    box-shadow: 0 2px 6px rgba(0,0,0,.25);
  }
  .card--services { top: 147px; }
  .card--contact { top: 433px; }

  .services__brand { position: absolute; left: 0; right: 0; top: 26px; text-align: center; }
  .card .brand-name { font-size: 54px; }
  .card--services .brand-legal { font-size: 11px; margin-top: 6px; }
  .services__abn { font-size: 11px; margin-top: 3px; }
  .services__heading {
    position: absolute; left: 24px; right: 24px; top: 144px;
    display: flex; align-items: center; gap: 12px;
    font-weight: 700; font-size: 14px; letter-spacing: .3px; white-space: nowrap;
  }
  .services__heading::before { content: ""; flex: 1; height: 1px; background: linear-gradient(90deg, transparent, var(--rule)); }
  .services__heading::after  { content: ""; flex: 1; height: 1px; background: linear-gradient(90deg, var(--rule), transparent); }
  .services__list {
    position: absolute; top: 168px; list-style: none; font-size: 10.5px; font-weight: 700; line-height: 12.7px;
  }
  .services__list--left { left: 28px; }
  .services__list--left li::before { content: "●"; font-size: 7px; margin-right: 6px; vertical-align: 1px; }
  .services__list--right { right: 26px; text-align: right; }
  .services__list--right li::after { content: "●"; font-size: 7px; margin-left: 6px; vertical-align: 1px; }
  .services__web { position: absolute; left: 0; right: 0; top: 228px; text-align: center; font-size: 10.5px; font-weight: 700; }

  .contact__brand { position: absolute; left: 34px; top: 86px; }
  .card--contact .brand-legal { font-size: 9px; margin-top: 6px; }
  .contact__divider { position: absolute; left: 224px; top: 62px; width: 1px; height: 130px; background: #4a4a4a; }
  .contact__details { position: absolute; left: 242px; top: 64px; font-size: 10.5px; line-height: 12.8px; }
  .contact__name { color: var(--gold); font-weight: 700; font-size: 14px; line-height: 16px; }
  .contact__title { margin-bottom: 9px; }
  .contact__address { margin-bottom: 11px; }
  .contact__lines { list-style: none; }
  .contact__lines li { display: flex; align-items: center; gap: 6px; }
  .contact__lines .icon { width: 10px; height: 10px; }
</style>
</head>
<body>

<section class="letterhead">
  <div class="letterhead__tab"></div>
  <div class="letterhead__brand">
    <div class="brand-name">ORV</div>
    <div class="brand-legal">ORV Corporate &amp; Financial Services Pty Ltd</div>
  </div>
  <ul class="letterhead__contact">
    <li>+61 437 215 086
      <svg class="icon" viewBox="0 0 12 12"><path d="M3 1l2 2-1 1.5c.8 1.6 1.9 2.7 3.5 3.5L9 7l2 2-1.5 2C5 10.5 1.5 7 1 2.5z" fill="var(--gold)"/></svg></li>
    <li>neil@orv-example.com.au
      <svg class="icon" viewBox="0 0 12 12"><rect x="1" y="2.5" width="10" height="7" fill="var(--gold)"/><path d="M1 2.5l5 4 5-4" stroke="#fff" fill="none"/></svg></li>
    <li>61 (8) 8000 4731
      <svg class="icon" viewBox="0 0 12 12"><rect x="3" y="1" width="6" height="3" fill="var(--gold)"/><rect x="1" y="4.5" width="10" height="5" rx="1" fill="var(--gold)"/><rect x="3" y="8" width="6" height="3" fill="var(--gold)" stroke="#fff" stroke-width=".6"/></svg></li>
    <li>neil7312
      <svg class="icon" viewBox="0 0 12 12"><rect x="1" y="1" width="10" height="10" rx="2" fill="var(--gold)"/></svg></li>
  </ul>

  <div class="letter">
    <p class="letter__date">[Pick the date]</p>
    <p>On the Insert tab, the galleries include items that are designed to coordinate with the overall look of your document. You can use these galleries to insert tables, headers, footers, lists, cover pages, and other document building blocks. When you create pictures, charts, or diagrams, they also coordinate with your current document look.</p>
    <p>You can easily change the formatting of selected text in the document text by choosing a look for the selected text from the Quick Styles gallery on the Home tab. You can also format text directly by using the other controls on the Home tab. Most controls offer a choice of using the look from the current theme or using a format that you specify directly.</p>
    <p>To change the overall look of your document, choose new Theme elements on the Page Layout tab. To change the looks available in the Quick Style gallery, use the Change Current Quick Style Set command. Both the Themes gallery and the Quick Styles gallery provide reset commands so that you can always restore the look of your document to the original contained in your current template.</p>
    <p>On the Insert tab, the galleries include items that are designed to coordinate with the overall look of your document. You can use these galleries to insert tables, headers, footers, lists, cover pages, and other document building blocks. When you create pictures, charts, or diagrams, they also coordinate with your current document look.</p>
    <p>On the Insert tab, the galleries include items that are designed to coordinate with the overall look of your document. You can use these galleries to insert tables, headers, footers, lists, cover pages, and other document building blocks. When you create pictures, charts, or diagrams, they also coordinate with your current document look.</p>
    <p>[Type the closing]</p>
    <div class="signature-area" role="img" aria-label="Handwritten signature of the sender"></div>
    <div class="letter__sender">
      <p>Name Lastname</p>
      <p>[Type the sender title]</p>
      <p>[Type the sender company name]</p>
    </div>
  </div>
  <div class="letterhead__footer">17 Wattlebank Road Wattlebank SA 5164</div>
</section>

<section class="card card--services">
  <div class="services__brand">
    <div class="brand-name">ORV</div>
    <div class="brand-legal">ORV Corporate &amp; Financial Services Pty Ltd</div>
    <div class="services__abn">ABN 71 384 902 157</div>
  </div>
  <h2 class="services__heading">OUR SERVICES</h2>
  <ul class="services__list services__list--left">
    <li>Corporate Finance</li>
    <li>Taxation</li>
    <li>Research &amp; Development Specialisation</li>
    <li>Financial Accounting</li>
  </ul>
  <ul class="services__list services__list--right">
    <li>Mergers &amp; Acquisitions</li>
    <li>Company Listings (IPO's)</li>
    <li>Business Valuations</li>
    <li>Capital Raising</li>
  </ul>
  <div class="services__web">www.orv-example.com.au</div>
</section>

<section class="card card--contact">
  <div class="contact__brand">
    <div class="brand-name">ORV</div>
    <div class="brand-legal">ORV Corporate &amp; Financial Services Pty Ltd</div>
  </div>
  <div class="contact__divider"></div>
  <div class="contact__details">
    <div class="contact__name">Neil Barrow</div>
    <div class="contact__title">Chartered Accountant</div>
    <div class="contact__address">17 Wattlebank Road<br>Wattlebank SA 5164</div>
    <ul class="contact__lines">
      <li><svg class="icon" viewBox="0 0 12 12"><path d="M3 1l2 2-1 1.5c.8 1.6 1.9 2.7 3.5 3.5L9 7l2 2-1.5 2C5 10.5 1.5 7 1 2.5z" fill="var(--gold)"/></svg>+61 437 215 086</li>
      <li><svg class="icon" viewBox="0 0 12 12"><rect x="1" y="2.5" width="10" height="7" fill="var(--gold)"/><path d="M1 2.5l5 4 5-4" stroke="var(--card)" fill="none"/></svg>neil@orv-example.com.au</li>
      <li><svg class="icon" viewBox="0 0 12 12"><rect x="3" y="1" width="6" height="3" fill="var(--gold)"/><rect x="1" y="4.5" width="10" height="5" rx="1" fill="var(--gold)"/></svg>61 (8) 8000 4731</li>
      <li><svg class="icon" viewBox="0 0 12 12"><rect x="1" y="1" width="10" height="10" rx="2" fill="var(--gold)"/></svg>neil7312</li>
    </ul>
  </div>
</section>

</body>
</html>
```